Premium modern eliquids labels 84.5 x 80 mm

I am looking for modern graphics for the labels of a new eliquid line that will have 4 different types of eliquids. It will have a tobacco one (brown colours maybe), a fruity one (bright colours maybe), a minty one (green colours maybe) and a creamy one (beige colours maybe).
I will need one of them to see how the design is, that design will have to be adapted to the other 3 colours of the label.
The brand logo is attached. I also attached a sample of what is mandatory to write on the label, you can change size, place and font of what is written, the only thing that cannot be reduced is the yellow parts. I attach the bottle that we will use.The size of the label is 84.5 x 80 mm (base x height).

Target Market(s)

vapers

Requirements
Must have
• My project must have one of the labels.

```html
<!DOCTYPE html>
<html lang="it">
<head>
<meta charset="utf-8">
<title>Lumen Vapour – etichette</title>
<link rel="stylesheet" href="https://fonts.googleapis.com/css2?family=Comfortaa:wght@400;700&family=Montserrat:wght@700;900&display=swap">
<style>
  :root {
    --bg: #ffffff;
    --label-bg: #000000;
    --text: #ffffff;
    --fruity-accent: #b65fd0;
    --fruity-hot: #e0219a;
    --fruity-art-a: #9b4fd3;
    --fruity-art-b: #e52d9a;
    --tobacco-accent: #b98a3e;
    --tobacco-art-a: #c79a4f;
    --tobacco-art-b: #8e8478;
  }
  * { box-sizing: border-box; margin: 0; padding: 0; }
  html, body { width: 1200px; height: 1200px; overflow: hidden; background: var(--bg); }
  body { position: relative; font-family: "Comfortaa", sans-serif; color: var(--text); }

  .label {
    position: absolute; top: 364px; width: 501px; height: 473px;
    background: var(--label-bg); overflow: hidden;
  }
  .label--fruity { left: 75px; --accent: var(--fruity-accent); --hot: var(--fruity-hot); --art-a: var(--fruity-art-a); --art-b: var(--fruity-art-b); }
  .label--tobacco { left: 615px; --accent: var(--tobacco-accent); --hot: var(--tobacco-accent); --art-a: var(--tobacco-art-a); --art-b: var(--tobacco-art-b); }

  .label__art {
    position: absolute; left: 100px; top: 0; width: 258px; height: 225px;
    border-radius: 0 0 110px 110px;
    background: linear-gradient(120deg, var(--art-a), var(--art-b));
    opacity: .85;
  }
  .label--tobacco .label__art { border-radius: 0 0 130px 130px; }

  .block { position: absolute; font-size: 12px; line-height: 14.5px; letter-spacing: -.2px; }
  .block__title { color: var(--accent); font-weight: 700; }

  .ingredients { left: 16px; top: 16px; }
  .usage { left: 398px; top: 16px; width: 95px; }

  .lot {
    position: absolute; left: 6px; top: 350px; transform-origin: 0 0; transform: rotate(-90deg);
    font-size: 9px; white-space: nowrap; letter-spacing: -.3px;
  }

  .flavour-name {
    position: absolute; left: 268px; top: 218px; font-size: 26px; color: var(--hot);
  }
  .label--tobacco .flavour-name { left: 232px; color: var(--accent); }

  .brand {
    position: absolute; left: 140px; top: 272px; width: 230px;
    display: flex; align-items: center; justify-content: center; gap: 10px;
  }
  .brand__dot { width: 14px; height: 14px; border-radius: 50%; background: var(--hot); }
  .brand__name { font-family: "Comfortaa", sans-serif; font-weight: 700; font-size: 30px; color: var(--text); letter-spacing: 1px; }

  .disposal { position: absolute; left: 408px; font-family: "Montserrat", sans-serif; font-weight: 700; }
  .disposal__head { font-size: 11px; line-height: 9px; }
  .disposal__part { font-size: 8px; margin-top: 3px; }
  .disposal__code { font-size: 12px; font-weight: 900; margin-top: 6px; margin-left: 4px; }
  .disposal--label { top: 232px; }
  .disposal--bottle { top: 302px; }

  .eco-icons { position: absolute; left: 400px; top: 386px; display: flex; gap: 8px; }
  .eco-icons span { width: 34px; height: 34px; border: 2px solid var(--accent); border-radius: 50%; }
  .eco-icons span + span { border-radius: 4px; }

  .maker { position: absolute; left: 16px; top: 358px; font-size: 9.5px; line-height: 10.5px; color: var(--accent); }
  .maker__head { font-size: 11.5px; line-height: 11px; }

  .volume {
    position: absolute; left: 0; width: 501px; top: 424px; padding-left: 0; text-align: center;
    font-family: "Montserrat", sans-serif; font-weight: 700; font-size: 11px; color: var(--hot);
  }
  .label--tobacco .volume { color: var(--accent); }
</style>
</head>
<body>

<section class="label label--fruity">
  <div class="label__art" role="img" aria-label="Line illustration of a grape bunch and an apple in purple-pink gradient"></div>
  <div class="block ingredients"><div class="block__title">INGREDIENTI:</div>Glicole<br>Propilenico<br>Sostanze<br>Aromatizzanti</div>
  <div class="block usage"><div class="block__title">ISTRUZIONI<br>D'USO:</div>Agitare bene prima dell'utilizzo. Diluire nelle percentuali consigliate sul nostro sito. Conservare in luogo fresco e asciutto</div>
  <div class="lot">L SH20 - 001-PES-D.PRO 22-04-2022 D.SC 21-04-2024</div>
  <div class="flavour-name">fruity</div>
  <div class="brand"><span class="brand__dot"></span><span class="brand__name">LUMEN VAPOUR</span></div>
  <div class="disposal disposal--label"><div class="disposal__head">RACCOLTA<br>PLASTICA</div><div class="disposal__part">ETICHETTA</div><div class="disposal__code">PAP 5</div></div>
  <div class="disposal disposal--bottle"><div class="disposal__head">RACCOLTA<br>PLASTICA</div><div class="disposal__part">FLACONE</div><div class="disposal__code">PET 1</div></div>
  <div class="eco-icons"><span></span><span></span></div>
  <div class="maker"><div class="maker__head">PRODOTTO<br>E CONFEZIONATO<br>DA Nebbia srl</div>Via Lago 18<br>10100 Torino<br>P.I.00000000000<br>Tel. +39 000 0000000<br>info@nebbia.it</div>
  <div class="volume">20 ML NET</div>
</section>

<section class="label label--tobacco">
  <div class="label__art" role="img" aria-label="Line illustration of two tobacco leaves in gold-grey gradient"></div>
  <div class="block ingredients"><div class="block__title">INGREDIENTI:</div>Glicole<br>Propilenico<br>Sostanze<br>Aromatizzanti</div>
  <div class="block usage"><div class="block__title">ISTRUZIONI<br>D'USO:</div>Agitare bene prima dell'utilizzo. Diluire nelle percentuali consigliate sul nostro sito. Conservare in luogo fresco e asciutto</div>
  <div class="lot">L SH20 - 001-PES-D.PRO 22-04-2022 D.SC 21-04-2024</div>
  <div class="flavour-name">tobacco</div>
  <div class="brand"><span class="brand__dot"></span><span class="brand__name">LUMEN VAPOUR</span></div>
  <div class="disposal disposal--label"><div class="disposal__head">RACCOLTA<br>PLASTICA</div><div class="disposal__part">ETICHETTA</div><div class="disposal__code">PAP 5</div></div>
  <div class="disposal disposal--bottle"><div class="disposal__head">RACCOLTA<br>PLASTICA</div><div class="disposal__part">FLACONE</div><div class="disposal__code">PET 1</div></div>
  <div class="eco-icons"><span></span><span></span></div>
  <div class="maker"><div class="maker__head">PRODOTTO<br>E CONFEZIONATO<br>DA Nebbia srl</div>Via Lago 18<br>10100 Torino<br>P.I.00000000000<br>Tel. +39 000 0000000<br>info@nebbia.it</div>
  <div class="volume">20 ML NET</div>
</section>

</body>
</html>
```